New Pain Management Physcian Private Practice webpage design

Interventional Pain Management Company looking for new website. Want it modeled very closely to http://www.brivoltclinic.example/ website. Under navigation panel at top of main webpage take off the following tabs: About, Locations, News, Testimonial, and Pain Channel. Add New Patient visit tab, change about to Main Page, change treatments to Procedures, change Providers to Provider.Main web page should have the KTR logo, no picture slideshow for now but want ability to add pictures to the slideshow in the future. Pictures are included to show you an idea of what main page should look like. Colors are teal,Deep Navy, and White as shown in KTR logo. Font style should also be same as KTR logo.

Target Market(s)

Patients with all kinda of acute and chronic pain. Especially neck, mid back,low back pain, and joint pain.

Industry/Entity Type

Medical

Coding

Number of Pages Required

5+ page

Requirements
Must have
• See Project description above
Nice to have
• ability to add pictures to the slideshow in future
Should not have
• not applicable

```html
<!DOCTYPE html>
<html lang="en">
<head>
<meta charset="utf-8">
<title>KTR Pain Management Center</title>
<link href="https://fonts.googleapis.com/css2?family=Open+Sans:wght@400;600;700&family=Oswald:wght@400;600&display=swap" rel="stylesheet">
<style>
:root{
  --teal:#2aa3b3;
  --teal-dark:#1d8795;
  --navy:#0f2236;
  --ink:#222;
  --muted:#6b6b6b;
  --light:#eef1f2;
  --band:#1f1f1f;
  --footer:#0b0b0b;
  --white:#fff;
}
*{box-sizing:border-box;margin:0;padding:0}
html,body{width:878px;height:1200px;overflow:hidden}
body{font-family:"Open Sans",Arial,sans-serif;color:var(--ink);background:var(--white);font-size:10px;line-height:1.45}
.site-header{height:92px;background:var(--light);position:relative}
.brand{position:absolute;left:70px;top:20px;display:flex;align-items:center;gap:8px}
.brand-mark{width:30px;height:30px;border-radius:50%;background:var(--teal)}
.brand-name{font-family:"Oswald",sans-serif;font-weight:600;font-size:20px;color:var(--navy);letter-spacing:1px}
.header-phone{position:absolute;left:330px;top:14px;font-size:16px;color:var(--teal);font-weight:700;display:flex;align-items:center;gap:6px}
.header-actions{position:absolute;right:70px;top:48px;display:flex;gap:6px}
.header-actions a{background:var(--teal);color:var(--white);font-size:8px;font-weight:700;padding:5px 10px;text-decoration:none;text-transform:uppercase}
.header-actions a.portal{background:var(--navy)}
.main-nav{height:18px;background:var(--white);border-bottom:1px solid #ddd;display:flex;justify-content:space-between;padding:0 70px;align-items:center;position:absolute;left:0;right:0;bottom:0}
.main-nav a{font-size:8px;font-weight:700;color:var(--muted);text-decoration:none;text-transform:uppercase}
.main-nav a.active{color:var(--navy)}
.hero{height:262px;background:linear-gradient(90deg,#f4f4f4,#e9eded);position:relative}
.hero-photo{position:absolute;left:0;top:0;width:330px;height:262px;background:linear-gradient(135deg,#e7d2c4,#d9b8a6 60%,#cfd6d8)}
.hero-copy{position:absolute;left:390px;top:68px;width:420px;text-align:right}
.hero-copy h1{font-family:"Oswald",sans-serif;font-weight:600;font-size:30px;color:var(--teal);margin-bottom:12px}
.hero-copy p{font-size:9px;color:var(--muted);margin-bottom:16px}
.btn-dark{display:inline-block;background:var(--ink);color:var(--white);font-size:9px;font-weight:700;padding:7px 14px;text-transform:uppercase;text-decoration:none}
.columns{display:flex;gap:40px;padding:28px 70px 0;height:460px}
.col{flex:1}
.col-label{font-size:12px;color:var(--ink)}
.col-title{font-family:"Oswald",sans-serif;font-size:30px;color:var(--teal);line-height:1;margin-bottom:12px;text-transform:uppercase}
.col h3{font-size:9px;font-weight:700;margin-bottom:8px}
.col p{font-size:9px;color:var(--muted);margin-bottom:12px}
.btn-outline{display:inline-block;border:1px solid #bbb;padding:6px 12px;font-size:9px;color:var(--ink);text-decoration:none;margin-bottom:22px}
.hours h4{font-family:"Oswald",sans-serif;color:var(--teal);font-size:16px;font-weight:400}
.hours p{margin-bottom:2px;color:var(--ink)}
.quick-links{list-style:none;margin-top:22px}
.quick-links li{font-size:8px;text-transform:uppercase;margin-bottom:5px;display:flex;gap:6px;align-items:center}
.quick-links li::before{content:"";width:5px;height:5px;background:var(--teal)}
.news-list{list-style:none;margin-bottom:12px}
.news-list li{display:flex;gap:8px;margin-bottom:10px;font-size:9px;color:var(--teal-dark)}
.news-list svg{flex:none;margin-top:3px}
.doctor-photo{width:100%;height:230px;background:linear-gradient(180deg,#cfd7dd,#8a9aa8)}
.doctor-name{font-size:9px;font-weight:700;margin-top:8px;text-transform:uppercase}
.doctor-bio{font-size:8px;color:var(--muted)}
.appointment{height:150px;background:var(--band);padding:22px 70px;color:var(--white)}
.appointment h2{font-size:12px;font-weight:700;text-transform:uppercase;margin-bottom:10px}
.appt-form{display:flex;gap:8px}
.appt-fields{display:grid;grid-template-columns:1fr 1fr 1fr;grid-template-rows:28px 28px;gap:8px;flex:1}
.field{background:var(--white);color:#999;font-size:8px;padding:7px}
.field.message{grid-row:span 2}
.appt-submit{width:130px;background:var(--teal);color:var(--white);font-size:10px;font-weight:700;display:flex;align-items:center;justify-content:center;text-align:center;text-transform:uppercase}
.site-footer{height:236px;background:var(--footer);color:#ccc;padding:26px 70px;display:flex;gap:40px}
.footer-col h4{font-size:10px;color:var(--teal);font-weight:700;text-transform:uppercase;margin-bottom:10px}
.footer-treat{flex:1.4}
.treat-grid{display:grid;grid-template-columns:1fr 1fr;font-size:8px;line-height:1.7}
.footer-links{flex:1;display:grid;grid-template-columns:1fr 1fr;font-size:8px;line-height:2.4;text-transform:uppercase;align-content:start;border-left:1px solid #333;padding-left:20px}
.footer-connect{flex:1;border-left:1px solid #333;padding-left:20px}
.socials{display:flex;gap:6px;margin-bottom:10px}
.socials span{width:14px;height:14px;border-radius:50%;background:#bbb}
.copyright{font-size:8px;color:#777}
.footer-extra{font-size:8px;color:var(--teal);margin-top:12px}
</style>
</head>
<body>
<header class="site-header">
  <div class="brand"><span class="brand-mark"></span><span class="brand-name">BRIVOLT</span></div>
  <div class="header-phone">
    <svg width="14" height="14" viewBox="0 0 24 24"><path fill="currentColor" d="M6.6 10.8a15 15 0 0 0 6.6 6.6l2.2-2.2c.3-.3.7-.4 1-.2 1.1.4 2.3.6 3.6.6.6 0 1 .4 1 1V20c0 .6-.4 1-1 1A17 17 0 0 1 3 4c0-.6.4-1 1-1h3.5c.6 0 1 .4 1 1 0 1.3.2 2.5.6 3.6.1.3 0 .7-.2 1z"/></svg>
    (555) Pain Center (555)-010-2468
  </div>
  <div class="header-actions">
    <a href="#">Request an appointment</a>
    <a href="#" class="portal">My portal</a>
    <a href="#">Refill treatment center</a>
  </div>
  <nav class="main-nav">
    <a href="#" class="active">Home</a><a href="#">New Patient Visit</a><a href="#">Provider</a><a href="#">Procedures</a><a href="#">Insurance</a><a href="#">FAQ</a><a href="#">Forms</a><a href="#">Contact</a>
  </nav>
</header>

<section class="hero">
  <div class="hero-photo" role="img" aria-label="Photo of a patient from behind holding the back of her neck in pain"></div>
  <div class="hero-copy">
    <h1>#1 PAIN MANAGEMENT CENTER</h1>
    <p>Our experienced team offers modern treatments for acute and chronic pain of the neck, mid back, low back and joints. We listen, build a plan around your goals and help you move through daily life again with more comfort and confidence.</p>
    <a href="#" class="btn-dark">Make appointment</a>
  </div>
</section>

<section class="columns">
  <div class="col">
    <div class="col-label">About</div>
    <div class="col-title">KTR</div>
    <h3>Manage your pain and get back into life.</h3>
    <p>KTR is a comprehensive pain management practice serving patients with neck, back and joint pain. Our physician will review your history, explain your options and guide you toward lasting relief.</p>
    <a href="#" class="btn-outline">Read more</a>
    <div class="hours">
      <h4>OFFICE HOURS:</h4>
      <p>M-F 8:00 am - 5:00 pm</p>
      <p>Office closed from 12:00 pm - 1:00 pm</p>
    </div>
    <ul class="quick-links">
      <li>Meet the provider</li><li>Patient forms</li><li>FAQ</li><li>Accepted insurance</li><li>Request appointment</li>
    </ul>
  </div>
  <div class="col">
    <div class="col-label">Latest</div>
    <div class="col-title">News</div>
    <ul class="news-list">
      <li><svg width="10" height="8" viewBox="0 0 10 8"><path d="M0 4h8M5 1l3 3-3 3" stroke="#222" fill="none" stroke-width="1.4"/></svg>Manage your pain and get back into life: new options for chronic low back pain.</li>
      <li><svg width="10" height="8" viewBox="0 0 10 8"><path d="M0 4h8M5 1l3 3-3 3" stroke="#222" fill="none" stroke-width="1.4"/></svg>Manage your pain and get back into life with guided joint care.</li>
      <li><svg width="10" height="8" viewBox="0 0 10 8"><path d="M0 4h8M5 1l3 3-3 3" stroke="#222" fill="none" stroke-width="1.4"/></svg>Manage your pain and get back into life after neck injury.</li>
      <li><svg width="10" height="8" viewBox="0 0 10 8"><path d="M0 4h8M5 1l3 3-3 3" stroke="#222" fill="none" stroke-width="1.4"/></svg>Manage your pain and get back into life: what to expect at visit one.</li>
      <li><svg width="10" height="8" viewBox="0 0 10 8"><path d="M0 4h8M5 1l3 3-3 3" stroke="#222" fill="none" stroke-width="1.4"/></svg>Manage your pain and get back into life with simple daily stretches.</li>
      <li><svg width="10" height="8" viewBox="0 0 10 8"><path d="M0 4h8M5 1l3 3-3 3" stroke="#222" fill="none" stroke-width="1.4"/></svg>Manage your pain and get back into life: mid back pain explained.</li>
    </ul>
    <a href="#" class="btn-dark">See all</a>
  </div>
  <div class="col">
    <div class="col-label">Your</div>
    <div class="col-title">Doctor</div>
    <div class="doctor-photo" role="img" aria-label="Portrait photo of the practice physician in a suit"></div>
    <div class="doctor-name">Elias Varga MD</div>
    <div class="doctor-bio">Double Board Certified in PM&amp;R and Interventional Pain Management</div>
  </div>
</section>

<section class="appointment">
  <h2>Make appointment now !</h2>
  <div class="appt-form">
    <div class="appt-fields">
      <div class="field">Name*</div>
      <div class="field">Phone*</div>
      <div class="field message">Details here...</div>
      <div class="field">Email*</div>
      <div class="field">Best*</div>
    </div>
    <div class="appt-submit">Get your<br>appointment</div>
  </div>
</section>

<footer class="site-footer">
  <div class="footer-col footer-treat">
    <h4>The leading medical treatments for pain</h4>
    <div class="treat-grid">
      <span>Back Pain</span><span>Headaches</span>
      <span>Neck Pain</span><span>Cancer Pain</span>
      <span>Face Pain</span><span>Nerve Pain</span>
      <span>Knee Pain</span><span>Arthritis</span>
      <span>Sciatica Pain</span><span>Shingles</span>
      <span>Foot Surgical Pain</span><span>Fibromyalgia</span>
      <span>Pelvic Pain</span><span>Joint Injuries</span>
      <span>Hip Pain</span><span>Neuropathy</span>
    </div>
    <div class="footer-extra">Explore our care options</div>
  </div>
  <div class="footer-links">
    <span>Home</span><span>Insurance</span>
    <span>New Patient Visit</span><span>FAQ</span>
    <span>Provider</span><span>Forms</span>
    <span>Procedures</span><span>Contact</span>
  </div>
  <div class="footer-connect">
    <h4>Connect</h4>
    <div class="socials"><span></span><span></span><span></span><span></span></div>
    <div class="copyright">© 2024 KTR. All rights reserved.</div>
  </div>
</footer>
</body>
</html>
```